Poster Design Project

Our goal is to cover the front of our unit with advertising posters relating to the work that we undertake.
I have attached a photo showing the front of the unit.
Our intention is to cover the windows with a single piece of sheet metal and have these posters digitally printed and applied to the sheet of metal. Just to clarify, no glass and frames of the window will not be visible, they will be completely covered by the posters.
The task is to design 4 x large posters and 1 x small poster to cover all windows to the front of the unit.
At the moment, we only have the dimensions of the sheet metal that will cover the large windows, this being 2150mm (W) x 2550 mm (H).
The dimensions of the small window will follow.
Please take some inspiration from our website as to how we like these posters to look. Generally speaking, a darker background with lighter font will make the poster more legible.
High definition pictures of the work we have done have been attached.
Contact details can be found on our website, although the address will be 57 Harrowden Lane, Slough, SL3 8TW. Telephone and email stay the same.
We would like facebook and twitter logos to appear on the boards also.
Layout (when looking at attached photo of front of unit):
- furthest left board to have contact details, facebook and twitter logos
- second from the left to advertise our wheel refurbishment services with associated pictures
-second from the right to advertise our window tinting services with associated pictures
- furthest to the right to have contact details, facebook and twitter logos
- window at the top to have our small "kp" logo
Opening hours also to be featured on boards showing contact details: Mon-Sat 8.30am - 5.30pm
Target Market(s)
The idea of the posters is to capture the attention of people driving by. Hence the posters must portray maximum amount of information in little time
Industry/Entity Type
Window Tinting

```html
<!DOCTYPE html>
<html lang="en">
<head>
<meta charset="utf-8">
<title>The Kerbpoint – Unit Front Posters</title>
<link rel="stylesheet" href="https://fonts.googleapis.com/css2?family=PT+Sans:wght@400;700&display=swap">
<style>
:root{
  --orange:#f7941d;
  --white:#ffffff;
  --header-top:#4a443d;
  --header-bottom:#2b2723;
  --slate-top:#5a5d60;
  --slate-bottom:#1f2629;
  --night:#1b2427;
  --photo-frame:#ffffff;
  --canvas:#ffffff;
}
*{box-sizing:border-box;margin:0;padding:0}
html,body{width:1200px;height:900px;overflow:hidden;background:var(--canvas)}
body{position:relative;font-family:"PT Sans",sans-serif;color:var(--white)}
.poster{position:absolute;top:26px;width:380px;height:450px;overflow:hidden}
.poster--contact{left:0}
.poster--wheels{left:413px}
.poster--tint{left:820px}
.brand-bar{position:absolute;left:0;top:0;width:100%;height:70px;
  background:linear-gradient(var(--header-top),var(--header-bottom))}
.brand{position:absolute;left:14px;top:9px;display:flex;align-items:center;gap:8px}
.brand-dot{width:14px;height:14px;border-radius:50%;background:var(--orange)}
.brand-name{font-size:34px;font-weight:400;line-height:1;color:var(--white)}
.brand-tagline{position:absolute;left:58px;top:52px;font-size:11px;letter-spacing:1px;color:var(--white);white-space:nowrap}

/* contact poster */
.contact-lines{position:absolute;left:0;top:70px;width:100%;height:126px;
  background:linear-gradient(var(--slate-top),var(--slate-bottom));text-align:center;padding-top:22px}
.tel{font-size:30px;font-weight:700;line-height:36px}
.tel span,.contact-small span{color:var(--orange)}
.contact-small{font-size:17px;font-weight:700;line-height:27px}
.social-band{position:absolute;left:0;top:196px;width:100%;height:113px;background:var(--orange);padding:8px 0 0 6px}
.social-row{display:flex;align-items:center;gap:6px;height:44px;font-size:22px;font-weight:700;color:var(--white);white-space:nowrap}
.social-square{flex:none;width:36px;height:36px;border-radius:6px;background:var(--night)}
.visit{position:absolute;left:0;top:309px;width:100%;height:141px;background:var(--night)}
.address{position:absolute;left:114px;top:34px;font-size:17px;font-weight:700;line-height:22px}
.mini-mark{position:absolute;left:300px;top:26px;display:flex;align-items:center;gap:5px}
.mini-mark .dot{width:10px;height:10px;border-radius:50%;background:var(--orange)}
.mini-mark .letters{font-size:34px;line-height:1;color:var(--white)}
.hours{position:absolute;left:38px;top:90px;font-size:22px;font-weight:700}

/* service posters */
.service-bg{position:absolute;left:0;top:70px;width:100%;height:380px;
  background:linear-gradient(var(--slate-top),var(--slate-bottom))}
.swoosh{position:absolute;left:0;top:70px}
.service-title{position:absolute;left:6px;top:88px;line-height:1}
.service-title .main{display:block;font-size:46px;font-weight:700;color:var(--white)}
.service-title .sub{display:block;font-size:32px;font-weight:700;color:var(--orange);margin-top:2px}
.photo{position:absolute;border:2px solid var(--photo-frame);border-radius:10px}

/* small window mark */
.window-mark{position:absolute;left:427px;top:500px;width:351px;height:400px;
  background:radial-gradient(circle at 50% 45%,#5a524a,#2f2a25);
  display:flex;align-items:center;justify-content:center;gap:14px}
.window-mark .dot{flex:none;width:34px;height:34px;border-radius:50%;background:var(--orange)}
.window-mark .letters{font-size:150px;font-weight:400;color:var(--white);line-height:1}
</style>
</head>
<body>

<section class="poster poster--contact">
  <header class="brand-bar">
    <div class="brand"><span class="brand-dot"></span><span class="brand-name">the kerbpoint</span></div>
    <div class="brand-tagline">CARE IN EVERY DETAIL</div>
  </header>
  <div class="contact-lines">
    <p class="tel">Tel: <span>01753 482917</span></p>
    <p class="contact-small">Email: <span>info@the-kerbpoint.com</span></p>
    <p class="contact-small">Web: <span>www.the-kerbpoint.com</span></p>
  </div>
  <div class="social-band">
    <p class="social-row"><span class="social-square"></span>friendspage.com/thekerbpoint</p>
    <p class="social-row"><span class="social-square"></span>chirpfeed.com/thekerbpoint</p>
  </div>
  <div class="visit">
    <p class="address">57 Harrowden Lane<br>Slough, SL3 8TW.</p>
    <div class="mini-mark"><span class="dot"></span><span class="letters">kp</span></div>
    <p class="hours">Open: Mon to Sat: 8.30 - 5.30</p>
  </div>
</section>

<section class="poster poster--wheels">
  <header class="brand-bar">
    <div class="brand"><span class="brand-dot"></span><span class="brand-name">the kerbpoint</span></div>
    <div class="brand-tagline">CARE IN EVERY DETAIL</div>
  </header>
  <div class="service-bg"></div>
  <svg class="swoosh" width="380" height="380" viewBox="0 0 380 380" aria-hidden="true">
    <path d="M380 0 L380 110 C300 190 150 250 0 262 L0 232 C150 210 250 150 268 0 Z" fill="var(--orange)"/>
  </svg>
  <h2 class="service-title"><span class="main">Wheel</span><span class="sub">Refurbishment</span></h2>
  <div class="photo" role="img" aria-label="Polished chrome alloy wheel" style="left:267px;top:56px;width:104px;height:106px;background:radial-gradient(#9a9a9a,#1a1a1a)"></div>
  <div class="photo" role="img" aria-label="Refurbished black wheel on an orange sports car" style="left:143px;top:190px;width:229px;height:229px;background:radial-gradient(circle at 50% 60%,#3a3a3a,#1c1c1c 60%,#d9822b)"></div>
  <div class="photo" role="img" aria-label="Silver multi-spoke alloy wheel" style="left:9px;top:320px;width:98px;height:99px;background:radial-gradient(#b8bcc0,#3a3f44)"></div>
</section>

<section class="poster poster--tint">
  <header class="brand-bar">
    <div class="brand"><span class="brand-dot"></span><span class="brand-name">the kerbpoint</span></div>
    <div class="brand-tagline">CARE IN EVERY DETAIL</div>
  </header>
  <div class="service-bg"></div>
  <svg class="swoosh" width="380" height="380" viewBox="0 0 380 380" aria-hidden="true">
    <path d="M380 0 L380 110 C300 190 150 250 0 262 L0 232 C150 210 250 150 268 0 Z" fill="var(--orange)"/>
  </svg>
  <h2 class="service-title"><span class="main">Window</span><span class="sub">Tinting</span></h2>
  <div class="photo" role="img" aria-label="Silver 4x4 with tinted rear windows" style="left:267px;top:54px;width:105px;height:106px;background:linear-gradient(#a9b3ba,#8c8a7c)"></div>
  <div class="photo" role="img" aria-label="White sports coupe with tinted side windows" style="left:143px;top:192px;width:229px;height:229px;background:linear-gradient(#6d7275 0,#e8eaea 45%,#cfd2d3 80%,#4b4e50)"></div>
  <div class="photo" role="img" aria-label="White saloon with tinted windows" style="left:10px;top:317px;width:100px;height:100px;background:linear-gradient(#3b3f42,#e6e7e7 55%,#9a9c9d)"></div>
</section>

<section class="window-mark" aria-label="The Kerbpoint mark">
  <span class="dot"></span>
  <span class="letters">kp</span>
</section>

</body>
</html>
```